Business Card Design

Selling Televisions, Velmora, Kira, Dravelux, Ronavi
The latest models, sizes ranging from 22"- 75"
Surround Sounds, Sound Bars and Wall Mounts

Target Market(s)

Mainly males/boys/blokes etc

Industry/Entity Type

Business

Contact Information for Business Card

Glen Marsh
07841526094
glmarsh@quinvale-mail.com

Requirements
Must have
• simplistic design, probably just 2 of the images used

clarity essential
Nice to have
• Metallic if possible

```html
<!DOCTYPE html>
<html lang="en">
<head>
<meta charset="utf-8">
<title>Glen Marsh – Business Card</title>
<link rel="stylesheet" href="https://fonts.googleapis.com/css2?family=Oswald:wght@400;600&display=swap">
<style>
  :root {
    --page-bg: #3b3634;
    --card-light: #5c6464;
    --card-mid: #2c3030;
    --card-dark: #0c0d0d;
    --text-main: #f2f2f2;
    --metal-top: #ffffff;
    --metal-bottom: #9aa0a2;
    --icon: #e8e8e8;
    --screen-sky-a: #f1c6c8;
    --screen-sky-b: #6f6a86;
    --screen-sky-c: #2c3440;
    --screen-city-a: #3a4a8c;
    --screen-city-b: #1a1c3a;
    --screen-city-c: #c27a3a;
    --bezel: #050505;
  }
  * { margin: 0; padding: 0; box-sizing: border-box; }
  html, body {
    width: 1200px;
    height: 840px;
    overflow: hidden;
    background: var(--page-bg);
  }
  .card {
    position: absolute;
    left: 100px;
    top: 90px;
    width: 1000px;
    height: 660px;
    background: radial-gradient(ellipse at 12% 0%, var(--card-light) 0%, var(--card-mid) 45%, var(--card-dark) 100%);
    font-family: 'Oswald', sans-serif;
    color: var(--text-main);
  }
  .holder-name {
    position: absolute;
    left: 79px;
    top: 160px;
    font-weight: 600;
    font-size: 56px;
    letter-spacing: 0.5px;
    line-height: 1;
    text-transform: uppercase;
    background: linear-gradient(180deg, var(--metal-top) 0%, var(--metal-top) 40%, var(--metal-bottom) 100%);
    -webkit-background-clip: text;
    background-clip: text;
    color: transparent;
  }
  .contact {
    position: absolute;
    left: 79px;
    display: flex;
    align-items: center;
    gap: 14px;
    font-size: 29px;
    font-weight: 400;
    line-height: 1;
  }
  .contact-phone { top: 263px; }
  .contact-email { top: 313px; }
  .contact svg { flex: none; }
  .offer-list {
    position: absolute;
    left: 82px;
    top: 418px;
    list-style: none;
  }
  .offer-list li {
    display: flex;
    align-items: center;
    gap: 14px;
    font-size: 22px;
    line-height: 1;
    height: 44.5px;
  }
  .screen {
    position: absolute;
    border: 6px solid var(--bezel);
    box-shadow: 0 8px 18px rgba(0,0,0,0.55);
  }
  .screen-landscape {
    left: 537px;
    top: 172px;
    width: 348px;
    height: 228px;
    background: linear-gradient(180deg, var(--screen-sky-a) 0%, var(--screen-sky-b) 45%, var(--screen-sky-c) 100%);
  }
  .screen-city {
    left: 700px;
    top: 312px;
    width: 242px;
    height: 190px;
    background: linear-gradient(180deg, var(--screen-city-a) 0%, var(--screen-city-b) 45%, var(--screen-city-c) 100%);
  }
</style>
</head>
<body>
  <main class="card">
    <h1 class="holder-name">Glen Marsh</h1>

    <p class="contact contact-phone">
      <svg width="20" height="30" viewBox="0 0 20 30" aria-hidden="true">
        <rect x="2" y="1.5" width="16" height="27" rx="3" fill="none" stroke="var(--icon)" stroke-width="2.5"/>
        <rect x="5.5" y="5" width="9" height="16" fill="var(--icon)"/>
        <circle cx="10" cy="24.5" r="1.6" fill="var(--icon)"/>
      </svg>
      <span>07841526094</span>
    </p>

    <p class="contact contact-email">
      <svg width="30" height="22" viewBox="0 0 30 22" aria-hidden="true">
        <rect x="0" y="0" width="30" height="22" fill="var(--icon)"/>
        <path d="M1 1 L15 12 L29 1" fill="none" stroke="var(--card-mid)" stroke-width="2"/>
        <path d="M1 21 L11 10 M29 21 L19 10" fill="none" stroke="var(--card-mid)" stroke-width="2"/>
      </svg>
      <span>glmarsh@quinvale-mail.com</span>
    </p>

    <ul class="offer-list">
      <li>
        <svg width="22" height="22" viewBox="0 0 22 22" aria-hidden="true"><g fill="var(--icon)"><path d="M11 0 L15 5 H7Z M11 22 L7 17 H15Z M0 11 L5 7 V15Z M22 11 L17 15 V7Z"/><circle cx="11" cy="11" r="2.5"/></g></svg>
        <span>Selling Televisions, Velmora, Kira, Dravelux, Ronavi</span>
      </li>
      <li>
        <svg width="22" height="22" viewBox="0 0 22 22" aria-hidden="true"><g fill="var(--icon)"><path d="M11 0 L15 5 H7Z M11 22 L7 17 H15Z M0 11 L5 7 V15Z M22 11 L17 15 V7Z"/><circle cx="11" cy="11" r="2.5"/></g></svg>
        <span>The latest models, sizes ranging from 22"- 75"</span>
      </li>
      <li>
        <svg width="22" height="22" viewBox="0 0 22 22" aria-hidden="true"><g fill="var(--icon)"><path d="M11 0 L15 5 H7Z M11 22 L7 17 H15Z M0 11 L5 7 V15Z M22 11 L17 15 V7Z"/><circle cx="11" cy="11" r="2.5"/></g></svg>
        <span>Surround Sounds, Sound Bars and Wall Mounts</span>
      </li>
    </ul>

    <div class="screen screen-landscape" role="img" aria-label="Flat-screen television showing a lake with rocky islands at dusk"></div>
    <div class="screen screen-city" role="img" aria-label="Curved television showing a city skyline lit at night"></div>
  </main>
</body>
</html>
```